Business Card for Web Design consulting firm

Business card designs for Web Design consulting firm

Target Market(s)

English speaking adults ages 30 - 60. Predominantly professional services eg. Doctor, Dentist

Industry/Entity Type

Consulting

Requirements
Must have
• Double sided card

```html
<!DOCTYPE html>
<html lang="en">
<head>
<meta charset="utf-8">
<title>Corvane Business Card</title>
<link rel="stylesheet" href="https://fonts.googleapis.com/css2?family=EB+Garamond:wght@400;500&display=swap">
<style>
  :root {
    --card-light: #f2f2f2;
    --charcoal: #4d4d4d;
    --orange: #f79a22;
    --gap: #ffffff;
    --text-dark: #4a4a4a;
  }
  * { margin: 0; padding: 0; box-sizing: border-box; }
  html, body {
    width: 887px;
    height: 1200px;
    overflow: hidden;
    background: var(--gap);
  }
  body {
    position: relative;
    font-family: "EB Garamond", Garamond, Georgia, serif;
  }
  .card {
    position: absolute;
    left: 0;
    width: 887px;
    height: 574px;
  }
  .card-front {
    top: 0;
    background: var(--card-light);
  }
  .card-back {
    top: 626px;
    overflow: hidden;
  }
  .brand-name {
    position: absolute;
    left: 36px;
    top: 70px;
    display: flex;
    align-items: center;
    gap: 14px;
    font-size: 52px;
    font-weight: 500;
    letter-spacing: 6px;
    color: var(--charcoal);
    line-height: 1;
  }
  .brand-square {
    width: 30px;
    height: 30px;
    background: var(--orange);
  }
  .person-name {
    position: absolute;
    left: 524px;
    top: 133px;
    font-size: 42px;
    color: var(--text-dark);
    line-height: 1;
  }
  .person-title {
    position: absolute;
    left: 605px;
    top: 188px;
    font-size: 32px;
    color: var(--orange);
    line-height: 1;
  }
  .contact-list {
    position: absolute;
    left: 605px;
    top: 374px;
    list-style: none;
    font-size: 28px;
    line-height: 35.5px;
    color: var(--text-dark);
  }
  .quadrant {
    position: absolute;
    width: 443.5px;
    height: 287px;
  }
  .quadrant-tl { left: 0; top: 0; background: var(--charcoal); }
  .quadrant-tr { left: 443.5px; top: 0; background: var(--orange); }
  .quadrant-bl { left: 0; top: 287px; background: var(--orange); }
  .quadrant-br { left: 443.5px; top: 287px; background: var(--charcoal); }
  .back-brand {
    position: absolute;
    left: 0;
    right: 0;
    top: 287px;
    transform: translateY(-50%);
    text-align: center;
    font-size: 128px;
    font-weight: 500;
    letter-spacing: 14px;
    color: var(--card-light);
    line-height: 1;
  }
</style>
</head>
<body>
  <section class="card card-front">
    <div class="brand-name"><span class="brand-square"></span>CORVANE</div>
    <h1 class="person-name">Daniel Harper</h1>
    <p class="person-title">Sales Manager</p>
    <ul class="contact-list">
      <li>P: 07 55501234</li>
      <li>M: 0455501234</li>
      <li>@: info@corvane.com</li>
      <li>www.corvane.com</li>
    </ul>
  </section>

  <section class="card card-back">
    <div class="quadrant quadrant-tl"></div>
    <div class="quadrant quadrant-tr"></div>
    <div class="quadrant quadrant-bl"></div>
    <div class="quadrant quadrant-br"></div>
    <div class="back-brand">CORVANE</div>
  </section>
</body>
</html>
```